BUSINESS CARD - HALVERDINE RURAL SERVICES

I would like to create a business card for my fertilizer spreading business. I would like to incorporate my existing logo and also a description of the services offered. The business card will be given to farmers so must be kept simple but effective. It will also be left in stores so much also be eye catching in order to stand out from other cards.

Target Market(s)

FARMERS

Requirements
Must have
• FRONT OF CARD = EXISTING LOGO + "CUSTOMISED SPREADING" below the logo

REAR Of CARD = SERVICES OFFERED AND CONTACT DETAILS

- Bulk fertilizer including Lime, Gypsum, Manure & Compost
- Granular fertilizer including Single Super, Urea, Nitro-am, & Custom Blends
- Modern equipment - Autosteer & Variable Rate Capable
- Friendly & Reliable Service
- Contact Gus: 0471 502 318
Nice to have
• utilize same color scheme as existing logo

```html
<!DOCTYPE html>
<html lang="en">
<head>
<meta charset="utf-8">
<title>Halverdine Rural Services – Business Card</title>
<link href="https://fonts.googleapis.com/css2?family=Maven+Pro:wght@400;500;700&display=swap" rel="stylesheet">
<style>
  :root {
    --page: #ffffff;
    --card-grey: #d9d7d8;
    --card-white: #ffffff;
    --charcoal: #5a5a5c;
    --ink: #4d4d4f;
    --orange: #f7941d;
    --band-text: #f2f2f2;
  }
  * { box-sizing: border-box; margin: 0; padding: 0; }
  html, body {
    width: 1200px; height: 1000px; overflow: hidden;
    background: var(--page);
    font-family: "Maven Pro", sans-serif;
    color: var(--ink);
  }
  .card {
    position: absolute; top: 350px;
    width: 525px; height: 300px;
    box-shadow: 3px 4px 10px rgba(0,0,0,0.22);
    overflow: hidden;
  }
  .card--front { left: 57px; background: var(--card-grey); }
  .card--back { left: 618px; background: var(--card-white); }

  .band {
    position: absolute; left: 0; right: 0; top: 236px; height: 37px;
    background: var(--charcoal);
    color: var(--band-text);
    display: flex; align-items: center;
  }
  .band--tagline {
    justify-content: center;
    font-size: 15px; letter-spacing: 3.4px; font-weight: 400;
  }
  .band--contact {
    justify-content: space-between;
    padding: 0 38px;
    font-size: 19px; font-weight: 500; letter-spacing: 0.8px;
  }

  .brand { position: absolute; text-align: center; }
  .brand__mark { display: block; margin: 0 auto; }
  .brand__name {
    font-weight: 700; color: var(--charcoal);
    white-space: nowrap; letter-spacing: -0.3px;
  }
  .card--front .brand { left: 0; right: 0; top: 44px; }
  .card--front .brand__name { font-size: 28px; margin-top: 14px; }
  .card--back .brand { left: 18px; width: 228px; top: 68px; }
  .card--back .brand__name { font-size: 17px; margin-top: 10px; }

  .services {
    position: absolute; left: 270px; top: 34px; width: 222px;
    list-style: none;
    font-size: 13.5px; line-height: 17.5px; letter-spacing: 0.3px;
  }
  .services li {
    position: relative; padding-left: 30px; margin-bottom: 10.5px;
  }
  .services li::before {
    content: ""; position: absolute; left: 5px; top: 4px;
    width: 10px; height: 10px; border-radius: 50%;
    background: var(--orange);
  }
  .services strong { font-weight: 700; display: block; }
</style>
</head>
<body>
  <section class="card card--front" aria-label="Business card front">
    <div class="brand">
      <svg class="brand__mark" width="116" height="116" viewBox="0 0 116 116" aria-hidden="true">
        <circle cx="58" cy="58" r="56" fill="var(--charcoal)"/>
      </svg>
      <div class="brand__name">Halverdine Rural Services</div>
    </div>
    <div class="band band--tagline">CUSTOMISED SPREADING</div>
  </section>

  <section class="card card--back" aria-label="Business card back">
    <div class="brand">
      <svg class="brand__mark" width="82" height="82" viewBox="0 0 82 82" aria-hidden="true">
        <circle cx="41" cy="41" r="40" fill="var(--charcoal)"/>
      </svg>
      <div class="brand__name">Halverdine Rural Services</div>
    </div>
    <ul class="services">
      <li><strong>Bulk fertilizer</strong>including Lime, Gypsum, Manure &amp; Composts</li>
      <li><strong>Granular fertilizer</strong>including Single Super, Urea, Nitro-am, &amp; Custom Blends</li>
      <li><strong>Modern equipment</strong></li>
      <li><strong>Friendly &amp; Reliable Service</strong></li>
    </ul>
    <div class="band band--contact">
      <span class="contact__name">Gus</span>
      <span class="contact__phone">0471 502 318</span>
    </div>
  </section>
</body>
</html>
```